Need Business Card for our Real Estate Business with Sales Executive's Picture

PANTONE 484 C ( RED)

PANTONE 2766 C ( BLUE

Industry/Entity Type

Real Estate

Contact Information for Business Card

Name, Mobile, email, & picture of Person
Agency Phone, address, Web address

Requirements
Must have
• Our Logo Colours, Agent Picture,

```html
<!DOCTYPE html>
<html lang="en">
<head>
<meta charset="utf-8">
<title>Mesa Ridge Realty – Business Card</title>
<link href="https://fonts.googleapis.com/css2?family=Lato:wght@400;700&display=swap" rel="stylesheet">
<style>
  :root {
    --stage: #3a3a3c;
    --navy: #262b45;
    --brand-red: #7e2a2c;
    --white: #ffffff;
    --ink: #1f2236;
  }
  * { box-sizing: border-box; margin: 0; padding: 0; }
  html, body { width: 1200px; height: 1200px; overflow: hidden; }
  body {
    background: var(--stage);
    font-family: "Lato", sans-serif;
    display: flex;
    flex-direction: column;
    align-items: center;
    justify-content: center;
    gap: 60px;
  }
  .card {
    position: relative;
    width: 840px;
    height: 480px;
    overflow: hidden;
    box-shadow: 0 10px 30px rgba(0,0,0,.45);
  }

  /* Front face */
  .card--front {
    background: var(--white);
    display: flex;
    flex-direction: column;
    align-items: center;
    justify-content: center;
    gap: 60px;
  }
  .brand-name {
    display: flex;
    align-items: center;
    gap: 18px;
    color: var(--ink);
    font-weight: 400;
    letter-spacing: 6px;
    text-transform: uppercase;
  }
  .brand-name__mark {
    width: 16px;
    height: 16px;
    background: var(--brand-red);
  }
  .card--front .brand-name { font-size: 52px; }
  .front-web {
    font-size: 22px;
    letter-spacing: 2px;
    color: var(--ink);
  }

  /* Back face */
  .card--back { background: var(--navy); }
  .back-curves { position: absolute; inset: 0; }
  .agent-photo {
    position: absolute;
    inset: 0;
    clip-path: path("M 452 0 C 340 150, 390 380, 610 480 L 840 480 L 840 0 Z");
    background:
      radial-gradient(ellipse 120px 150px at 660px 150px, #c79a7e 0%, #b98a70 55%, transparent 100%),
      linear-gradient(180deg, #ffffff 0%, #ffffff 40%, transparent 40%),
      radial-gradient(ellipse 240px 200px at 680px 470px, #2f4fa6 0%, #2a3f86 60%, transparent 100%),
      #ffffff;
  }
  .back-info {
    position: absolute;
    left: 80px;
    top: 70px;
    color: var(--white);
  }
  .card--back .brand-name {
    color: var(--white);
    font-size: 30px;
    letter-spacing: 4px;
  }
  .agent-name {
    margin-top: 90px;
    font-size: 32px;
    font-weight: 700;
    color: var(--brand-red);
  }
  .agent-title {
    font-size: 20px;
    margin-top: 2px;
  }
  .contact-list {
    list-style: none;
    margin-top: 24px;
    font-size: 21px;
    line-height: 30px;
  }
  .contact-list li {
    display: flex;
    align-items: center;
    gap: 18px;
  }
  .contact-list svg { width: 16px; height: 16px; fill: var(--brand-red); flex: none; }
  .address {
    margin-top: 16px;
    font-size: 23px;
  }
</style>
</head>
<body>

  <section class="card card--front">
    <div class="brand-name"><span class="brand-name__mark"></span>Mesa Ridge Realty</div>
    <p class="front-web">www.mesaridgerealty.com</p>
  </section>

  <section class="card card--back">
    <svg class="back-curves" viewBox="0 0 840 480" aria-hidden="true">
      <path d="M 404 0 C 290 160, 350 390, 566 480 L 610 480 C 390 380, 340 150, 452 0 Z" fill="var(--brand-red)"/>
      <path d="M 432 0 C 322 155, 372 385, 592 480 L 600 480 C 382 382, 332 152, 440 0 Z" fill="var(--navy)"/>
    </svg>
    <div class="agent-photo" role="img" aria-label="Portrait photo of the sales agent in a blue suit and striped tie"></div>

    <div class="back-info">
      <div class="brand-name"><span class="brand-name__mark"></span>Mesa Ridge</div>
      <h1 class="agent-name">Daniel Carver</h1>
      <p class="agent-title">Manager</p>
      <ul class="contact-list">
        <li><svg viewBox="0 0 16 16"><path d="M3 1l3 3-2 2c1 2 3 4 5 5l2-2 3 3-2 3C6 14 2 10 1 3z"/></svg>555 010 4200</li>
        <li><svg viewBox="0 0 16 16"><path d="M4 0h8v16H4z M5 2v10h6V2z"/></svg>555 010 4201</li>
        <li><svg viewBox="0 0 16 16"><path d="M0 3h16v10H0z M1 4l7 5 7-5"/></svg>info@mesaridgerealty.com</li>
        <li><svg viewBox="0 0 16 16"><circle cx="8" cy="8" r="8"/></svg>www.mesaridgerealty.com</li>
      </ul>
      <p class="address">48 Cedar Row, Austin, TX 78701</p>
    </div>
  </section>

</body>
</html>
```